Financial planning wealth advisor Business Card

We have a finanancial advisory that caters to high net worth and business owner clients. We would like a card that works with our entire style. Please visit out website larkfieldcapitalpartners.com to get a look and feel.... VERY OPEN to interesting and unique designs that have cutouts, fold overs, anything to capture interest...

Requirements, info must be the following:

Larkfield Capital Partners (with Logo)
Investments | Insurance | Retirement | Education | Estate | Business Planning

Nora Vesk Albright, CFP, MSFS, AEP
Principal

555-207-8160 (Main)
555-382-9045 (Cell)
ealbright@larkfieldcapitalpartners.com

Central Location:
218 W Palomar Suite 1400
El Paso TX 79814

West Location:
6132 Millbrook Lane SuiteB
El Paso TX 79836

larkfieldcapitalpartners.com

DISCLOSURES (Back of Card)
Eleanor Vesk Albright, CFP, MSFS, AEP, a Registered Representative offering securities through TORVANE Brokerage LLC. 218 W Palomar Suite 1400 El Paso TX 79814 555-619-4720. Member FINRA/SIPC, a licensed insurance agency.

*Financial Adviser offering investment advisory services through Harrow Advisory, LLC, a Registered Investment Advisor.

Larkfield Capital Partners is not owned or operated by TORVANE Brokerage LLC or its affiliates.

Target Market(s)

High end affluent or ultra rich clientele

Industry/Entity Type

Financial Planning

Font styles to use
Decorative

Requirements
Must have
• Needs to have something that focuses our services. :33 bellow for our original business card.

```html
<!DOCTYPE html>
<html lang="en">
<head>
<meta charset="utf-8">
<title>Larkfield Capital Partners — Business Card</title>
<link rel="stylesheet" href="https://fonts.googleapis.com/css2?family=Montserrat:wght@400;500;600;700&display=swap">
<style>
  :root {
    --bg: #e9e9ea;
    --card-white: #ffffff;
    --card-blue: #335b96;
    --navy: #2a4f8f;
    --gold: #d7ab5e;
    --ink: #1d1d1d;
    --grey: #8a8a8a;
    --white: #ffffff;
  }
  * { box-sizing: border-box; margin: 0; padding: 0; }
  html, body {
    width: 1200px; height: 900px; overflow: hidden;
    background: var(--bg);
    font-family: "Montserrat", sans-serif;
  }
  .canvas { position: relative; width: 1200px; height: 900px; }
  .card {
    position: absolute; width: 620px; height: 354px;
    border-radius: 26px;
    box-shadow: 0 10px 28px rgba(0,0,0,0.18);
    overflow: hidden;
  }
  /* Front card */
  .card-front { left: 90px; top: 70px; background: var(--card-white); }
  .brand {
    position: absolute; left: 42px; top: 118px; width: 240px;
    display: flex; align-items: center; gap: 12px;
  }
  .brand-dot {
    width: 30px; height: 30px; border-radius: 50%; background: var(--gold); flex: none;
  }
  .brand-name {
    font-size: 25px; font-weight: 500; color: var(--ink); line-height: 1.12; letter-spacing: 0.5px;
  }
  .front-contact { position: absolute; left: 330px; top: 66px; }
  .front-name { font-size: 20px; font-weight: 700; color: var(--navy); }
  .front-creds { font-size: 18px; color: var(--gold); margin-top: 4px; }
  .front-role { font-size: 13px; color: var(--grey); margin-top: 2px; }
  .front-phone {
    font-size: 15px; color: var(--navy); margin-top: 4px;
    display: flex; align-items: center; gap: 8px;
  }
  .front-phone svg { width: 12px; height: 12px; }
  .front-footer {
    position: absolute; left: 0; right: 0; bottom: 44px; text-align: center;
  }
  .disclosure { font-size: 15px; color: var(--gold); line-height: 1.35; }
  .services {
    font-size: 15.5px; font-weight: 500; color: var(--navy); line-height: 1.3;
    margin-top: 10px; letter-spacing: 0.3px;
  }
  /* Back card */
  .card-back { left: 490px; top: 476px; background: var(--card-blue); color: var(--white); }
  .back-brand {
    position: absolute; left: 40px; top: 140px; width: 220px;
    display: flex; align-items: center; gap: 12px;
  }
  .back-brand .brand-name { color: var(--gold); font-size: 24px; }
  .back-contact { position: absolute; left: 292px; top: 26px; }
  .back-name { font-size: 20px; font-weight: 600; color: var(--gold); }
  .back-creds { font-size: 20px; margin-top: 1px; }
  .back-role { font-size: 13px; margin-top: 1px; }
  .loc-label { font-size: 14px; font-weight: 600; color: var(--gold); margin-top: 6px; }
  .loc-line { font-size: 14px; line-height: 1.25; }
  .contact-list { list-style: none; margin-top: 14px; }
  .contact-list li {
    font-size: 14px; line-height: 1.4; display: flex; align-items: center; gap: 10px;
  }
  .contact-list svg { width: 12px; height: 12px; flex: none; }
</style>
</head>
<body>
<main class="canvas">
  <section class="card card-front">
    <div class="brand">
      <span class="brand-dot"></span>
      <span class="brand-name">Larkfield Capital Partners</span>
    </div>
    <div class="front-contact">
      <p class="front-name">Eleanor Vesk Albright</p>
      <p class="front-creds">CFP, MSFS, AEP,</p>
      <p class="front-role">Member</p>
      <p class="front-phone">
        <svg viewBox="0 0 24 24"><path fill="#d7ab5e" d="M6.6 10.8a15 15 0 0 0 6.6 6.6l2.2-2.2a1 1 0 0 1 1-.25 11.4 11.4 0 0 0 3.6.57 1 1 0 0 1 1 1V20a1 1 0 0 1-1 1A17 17 0 0 1 3 4a1 1 0 0 1 1-1h3.5a1 1 0 0 1 1 1c0 1.25.2 2.45.57 3.6a1 1 0 0 1-.25 1z"/></svg>
        555-619-4720
      </p>
    </div>
    <div class="front-footer">
      <p class="disclosure">A Registered Representative<br>Offering securities through TORVANE Brokerage LLC.</p>
      <p class="services">INVESTMENTS | INSURANCE | RETIREMENT<br>EDUCATION | ESTATE | BUSINESS PLANNING</p>
    </div>
  </section>

  <section class="card card-back">
    <div class="back-brand">
      <span class="brand-name">Larkfield Capital Partners</span>
    </div>
    <div class="back-contact">
      <p class="back-name">Nora Vesk Albright</p>
      <p class="back-creds">(CFP, MSFS, AEP)</p>
      <p class="back-role">Principal</p>
      <p class="loc-label">Central Location:</p>
      <p class="loc-line">218 W Palomar Suite 1400</p>
      <p class="loc-line">El Paso TX 79814</p>
      <p class="loc-label">West Location:</p>
      <p class="loc-line">6132 Millbrook Lane SuiteB</p>
      <p class="loc-line">El Paso TX 79836</p>
      <ul class="contact-list">
        <li><svg viewBox="0 0 24 24"><path fill="#d7ab5e" d="M6.6 10.8a15 15 0 0 0 6.6 6.6l2.2-2.2a1 1 0 0 1 1-.25 11.4 11.4 0 0 0 3.6.57 1 1 0 0 1 1 1V20a1 1 0 0 1-1 1A17 17 0 0 1 3 4a1 1 0 0 1 1-1h3.5a1 1 0 0 1 1 1c0 1.25.2 2.45.57 3.6a1 1 0 0 1-.25 1z"/></svg>555-207-8160</li>
        <li><svg viewBox="0 0 24 24"><rect x="6" y="2" width="12" height="20" rx="2" fill="none" stroke="#d7ab5e" stroke-width="2.4"/><circle cx="12" cy="18" r="1.4" fill="#d7ab5e"/></svg>555-382-9045</li>
        <li><svg viewBox="0 0 24 24"><rect x="2" y="5" width="20" height="14" rx="1.5" fill="none" stroke="#d7ab5e" stroke-width="2.4"/><path d="M2 6l10 7 10-7" fill="none" stroke="#d7ab5e" stroke-width="2.2"/></svg>ealbright@larkfieldcapitalpartners.com</li>
        <li><svg viewBox="0 0 24 24"><circle cx="12" cy="12" r="10" fill="none" stroke="#d7ab5e" stroke-width="2.4"/><path d="M2 12h20M12 2c3 3 3 17 0 20M12 2c-3 3-3 17 0 20" fill="none" stroke="#d7ab5e" stroke-width="1.8"/></svg>www.larkfieldcapitalpartners.com</li>
      </ul>
    </div>
  </section>
</main>
</body>
</html>
```